Varden Chamber Home Page - Make it more modern a little bit futuristic

Take existing site and make it more modern and a little bit futuristic.
Design of new homepage with slightly more futuristic feel.

I don't the current design. There has recently been a change of direction of the chamber partly driven by COVID to move more meetings online instead of face to face. We want to inspire our members to embrace technology. We also want to position our city as a great modern place to business. We want to do that by featuring our great members on the home page. We also want to promote events on the home page. We also want to convert new visitors to members.

Members should be able to login to manage their membership. Visitors should be able to search for members by category, member name, member company.

It should look premium corporate but more futuristic and forward looking than the neighbouring Chambers:
https://www.silverdunemidchamber.com.au/
https://www.thornbayheadlandchamber.org.au/
https://marrowfieldchamber.org.au/
https://saltgroveshorechamber.org.au/#!event-list
https://directory.businesskelvinharbourregion.com.au/businesses/n-t/ash-creeks-chamber-of-commerce

Target Market(s)

Modern small businesses owners

Industry/Entity Type

Business

Number of Pages Required

1 page

Font styles to use
Sans Serif

Requirements
Must have
• Appeal to small business owners
Responsive down to mobile
Nice to have
• Draw a focus to members from directory
Either a white background or black background
I really like the Bellmont Ridge Chamber home page at: https://bmrchamber.com/
Should not have
• Must look more modern than their existing site at: https://www.silverdunemidchamber.com.au/
No significant changes to logo
Don't like the light blue on existing site.

```html
<!DOCTYPE html>
<html lang="en">
<head>
<meta charset="utf-8">
<title>Varden Chamber of Commerce</title>
<link href="https://fonts.googleapis.com/css2?family=Poppins:wght@300;400;500;600&family=Cinzel:wght@400&display=swap" rel="stylesheet">
<style>
:root{
  --navy:#112a4e;
  --navy-deep:#0b1f3c;
  --gold:#f0b41c;
  --ink:#2b2b2b;
  --white:#ffffff;
  --field:#e6e6e6;
  --muted:#b9c3d3;
}
*{margin:0;padding:0;box-sizing:border-box}
html,body{width:1200px;height:2701px;overflow:hidden}
body{position:relative;font-family:'Poppins',sans-serif;color:var(--ink);background:var(--white)}
.abs{position:absolute}
/* hero */
.hero-photo{left:0;top:0;width:1200px;height:745px;
  background:linear-gradient(180deg,#1a2230 0%,#5e6a78 14%,#b9a27a 30%,#8f7a55 42%,#4f5a4a 52%,#3d5f7a 64%,#2c4a68 80%,#1d3450 100%)}
.hero-shade{left:0;top:0;width:1200px;height:140px;background:linear-gradient(180deg,rgba(10,14,22,.85),rgba(10,14,22,0))}
.hero-edge{left:0;top:600px;width:1200px;height:160px}
.topbar{top:20px;height:26px;display:flex;align-items:center;color:var(--white);font-size:17px}
.social{left:588px;gap:20px}
.social span{width:14px;height:14px;border:1.6px solid var(--white);border-radius:50%;display:block}
.top-links{left:771px;gap:29px;font-weight:300}
.top-phone{left:914px;gap:8px;font-weight:400;font-size:17px}
.logo{left:100px;top:46px;display:flex;align-items:center;gap:12px;color:var(--white)}
.logo-mark{width:70px;height:70px;background:var(--gold)}
.logo-name{font-family:'Poppins',sans-serif;font-weight:400;line-height:1}
.logo-name .big{display:block;font-size:42px;letter-spacing:3px}
.logo-name .small{display:block;font-size:14px;letter-spacing:1.5px;margin-top:4px}
.nav{left:491px;top:74px;width:609px;height:41px;border-bottom:1px solid rgba(255,255,255,.45);display:flex;justify-content:space-between;padding:0 12px;font-size:17px;color:var(--white);font-weight:300}
.nav a{color:inherit;text-decoration:none;position:relative}
.nav a.active{color:var(--gold)}
.nav a.active::after{content:"";position:absolute;left:-12px;right:-12px;top:38px;height:3px;background:var(--gold)}
.nav a.active::before{content:"";position:absolute;left:50%;top:41px;margin-left:-4px;border:4px solid transparent;border-top-color:var(--gold)}
.hero-title{left:0;width:1200px;text-align:center;font-family:'Cinzel',serif;color:var(--white);font-weight:400}
.hero-title.t1{top:214px;font-size:35px}
.hero-title.t2{top:272px;font-size:51px}
.search{left:192px;top:351px;width:816px;height:100px;background:#0c0c0c;padding:10px 24px;display:flex;gap:18px}
.search-field{display:flex;flex-direction:column;gap:6px;color:var(--white);font-size:15px}
.search-field .box{height:41px;background:var(--field);color:#4a4a4a;display:flex;align-items:center;justify-content:space-between;padding:0 18px;font-size:15px}
.explore{left:510px;top:480px;width:181px;height:51px;background:var(--navy);color:var(--white);font-size:19px;display:flex;align-items:center;justify-content:center;gap:12px;border-radius:2px}
/* welcome */
.welcome-title{left:121px;top:832px;font-size:34px;font-weight:600;line-height:44px;color:var(--ink)}
.welcome-copy{left:121px;top:948px;width:600px;font-size:14px;line-height:24px;font-weight:400;letter-spacing:-.1px}
.welcome-copy p+p{margin-top:9px}
.btn{background:var(--navy);color:var(--white);display:flex;align-items:center;justify-content:center;gap:8px;font-size:15px}
.learn{left:120px;top:1110px;width:148px;height:44px}
.welcome-photo{left:772px;top:833px;width:278px;height:279px;background:linear-gradient(135deg,#9aa3ad 0%,#4e5a6c 45%,#1f2c44 100%)}
/* services */
.services-band{left:0;top:1210px;width:1200px;height:720px}
.card{width:236px;text-align:center;padding:0 18px}
.card h3{font-size:16.5px;font-weight:600;margin:10px 0 12px}
.card p{font-size:12.3px;line-height:17.5px}
.card-solid{background:var(--white);color:var(--ink);box-shadow:0 6px 18px rgba(0,0,0,.25);clip-path:polygon(0 12px,100% 0,100% 100%,0 100%)}
.card-line{border:2px solid var(--white);color:var(--white)}
.card-line h3{color:var(--white)}
.icon{display:block;margin:0 auto}
/* b2b */
.b2b-title{left:224px;top:1974px;font-size:32px;font-weight:600;line-height:40px}
.b2b-copy{left:224px;top:2083px;width:760px;font-size:14.6px;line-height:28.8px}
/* footer */
.footer-band{left:0;top:2270px;width:1200px;height:431px}
.foot-col{color:var(--white)}
.foot-col h4{font-size:12.5px;font-weight:600;margin-bottom:10px;letter-spacing:.2px}
.foot-col li{list-style:none;font-size:12.5px;color:var(--muted);line-height:24px}
.contact-row{display:flex;gap:10px;font-size:12.5px;color:var(--muted);line-height:22px;margin-bottom:13px}
.foot-rule{left:0;top:2633px;width:1200px;height:1px;background:rgba(255,255,255,.35)}
.copyright{left:107px;top:2656px;font-size:12.5px;color:var(--muted)}
.foot-social{left:964px;top:2658px;display:flex;gap:14px}
.foot-social span{width:13px;height:13px;border:1.5px solid var(--muted);border-radius:50%;display:block}
</style>
</head>
<body>

<!-- hero -->
<div class="abs hero-photo" role="img" aria-label="City skyline at sunset beside a river with a bridge"></div>
<div class="abs hero-shade"></div>
<svg class="abs hero-edge" viewBox="0 0 1200 160" width="1200" height="160" aria-hidden="true">
  <polygon points="0,120 1200,10 1200,160 0,160" fill="var(--navy)"/>
  <polygon points="0,122 1200,12 1200,16 0,126" fill="var(--gold)"/>
  <polygon points="0,142 1200,34 1200,160 0,160" fill="var(--white)"/>
</svg>

<div class="abs topbar social"><span></span><span></span><span></span><span></span></div>
<div class="abs topbar top-links"><span>Join</span><span>Login</span></div>
<div class="abs topbar top-phone">
  <svg width="18" height="18" viewBox="0 0 24 24" fill="none" stroke="#fff" stroke-width="1.8"><path d="M5 3h4l2 5-2.5 1.5a11 11 0 0 0 6 6L16 13l5 2v4a2 2 0 0 1-2 2A16 16 0 0 1 3 5a2 2 0 0 1 2-2z"/></svg>
  <span>+61 7 3555 0148</span>
</div>

<div class="abs logo">
  <div class="logo-mark"></div>
  <div class="logo-name"><span class="big">VARDEN</span><span class="small">Chamber of Commerce</span></div>
</div>

<nav class="abs nav">
  <a class="active" href="#">Home</a><a href="#">Membership</a><a href="#">Events</a><a href="#">Benefits</a><a href="#">About Us</a><a href="#">Contact</a>
</nav>

<h1 class="abs hero-title t1">WELCOME TO VARDEN</h1>
<h2 class="abs hero-title t2">CHAMBER OF COMERCE</h2>

<form class="abs search">
  <label class="search-field" style="width:286px">Members Category<span class="box">Category Select<svg width="16" height="10" viewBox="0 0 16 10"><path d="M1 1l7 7 7-7" fill="none" stroke="#333" stroke-width="1.6"/></svg></span></label>
  <label class="search-field" style="width:268px">Member Name<span class="box">Name<svg width="16" height="10" viewBox="0 0 16 10"><path d="M1 1l7 7 7-7" fill="none" stroke="#333" stroke-width="1.6"/></svg></span></label>
  <label class="search-field" style="width:184px">Company<span class="box">Company<svg width="16" height="10" viewBox="0 0 16 10"><path d="M1 1l7 7 7-7" fill="none" stroke="#333" stroke-width="1.6"/></svg></span></label>
</form>

<div class="abs explore">Explore Now <svg width="8" height="12" viewBox="0 0 8 12"><path d="M0 0l8 6-8 6z" fill="#fff"/></svg></div>

<!-- welcome -->
<h2 class="abs welcome-title">Varden Chamber Welcomes<br>New Members</h2>
<div class="abs welcome-copy">
  <p>The Chamber provides support to Varden Business through enabling networking and interaction within the community, including Government, Council, Schools and Community Groups.</p>
  <p>The Chamber provides opportunities for you to meet and promote your business to a broad range of Varden businesses, community groups and government bodies.</p>
</div>
<div class="abs btn learn">Learn More <svg width="14" height="14" viewBox="0 0 14 14"><circle cx="7" cy="7" r="7" fill="#fff"/><path d="M5.5 4l3 3-3 3" fill="none" stroke="var(--navy)" stroke-width="1.6"/></svg></div>
<div class="abs welcome-photo" role="img" aria-label="Business team meeting around a conference table"></div>

<!-- services -->
<svg class="abs services-band" viewBox="0 0 1200 720" width="1200" height="720" aria-hidden="true">
  <polygon points="0,83 1200,7 1200,648 0,715" fill="var(--navy)"/>
</svg>

<div class="abs card card-solid" style="left:207px;top:1427px;height:230px;padding-top:30px">
  <svg class="icon" width="60" height="54" viewBox="0 0 60 54" fill="none" stroke="#222" stroke-width="2"><path d="M14 34a10 10 0 0 1 2-20 14 14 0 0 1 27-2 10 10 0 0 1 3 22"/><circle cx="30" cy="26" r="4"/><circle cx="20" cy="32" r="3.5"/><circle cx="40" cy="32" r="3.5"/><path d="M23 44v-6a7 7 0 0 1 14 0v6M13 48v-5a6 6 0 0 1 12 0M35 48v-5a6 6 0 0 1 12 0M10 50h40"/></svg>
  <h3>Member Directory</h3>
  <p>Equipped with storage, sorting, packing, warehousing fruits, and banana ripening at a large scale.</p>
</div>

<div class="abs card card-line" style="left:481px;top:1324px;height:232px;padding-top:30px">
  <svg class="icon" width="52" height="52" viewBox="0 0 52 52" fill="none" stroke="#fff" stroke-width="2.2"><rect x="3" y="7" width="46" height="42" rx="4"/><path d="M3 17h46M14 2v10M38 2v10"/><g fill="#fff" stroke="none"><rect x="10" y="23" width="6" height="4"/><rect x="19" y="23" width="6" height="4"/><rect x="28" y="23" width="6" height="4"/><rect x="37" y="23" width="6" height="4"/><rect x="10" y="31" width="6" height="4"/><rect x="19" y="31" width="6" height="4"/><rect x="28" y="31" width="6" height="4"/><rect x="37" y="31" width="6" height="4"/><rect x="10" y="39" width="6" height="4"/><rect x="19" y="39" width="6" height="4"/><rect x="28" y="39" width="6" height="4"/></g></svg>
  <h3>Upcoming Events</h3>
  <p>To facilitate the development of agricultural and food business by providing high quality produce for the consumers</p>
</div>

<div class="abs card card-line" style="left:481px;top:1588px;height:224px;padding-top:22px">
  <svg class="icon" width="50" height="50" viewBox="0 0 50 50" fill="none" stroke="#fff" stroke-width="2"><path d="M22 6a21 21 0 1 0 22 22H22z"/><path d="M28 2v20h20A20 20 0 0 0 28 2z"/></svg>
  <h3>Business 2 Business</h3>
  <p>To grow into a sustainable agriculture and food products provider by ensuring supply sufficiency, high quality farming</p>
</div>

<div class="abs card card-solid" style="left:758px;top:1427px;height:230px;padding-top:34px">
  <svg class="icon" width="76" height="52" viewBox="0 0 76 52" fill="none" stroke="#222" stroke-width="2"><path d="M2 10h10v24H2M74 10H64v24h10"/><path d="M12 14l12-6 10 4 8-4 12 2 10 4"/><path d="M64 30l-8 2-14 14a3 3 0 0 1-4-4M38 42l-4 4a3 3 0 0 1-4-4M30 42l-3 3a3 3 0 0 1-4-4M23 41l-2 2a3 3 0 0 1-4-4l-5-5"/><path d="M34 12l-10 8a3 3 0 0 0 4 4l8-5 18 15"/></svg>
  <h3>Join the Chamber</h3>
  <p>Red Delicious<br>Golden Delicious, Gala,<br>Royal Gala, Hayward Kiwi<br>SugarRed Kiwi</p>
</div>

<!-- b2b -->
<h2 class="abs b2b-title">Business 2 Business<br>A book and now a weekly webinar!!</h2>
<div class="abs b2b-copy">
  <p>Business 2 Business is a collaboration written by business members of Varden Chamber of Commerce.</p>
  <p>Our aim is to bring Business 2 your Business.</p>
  <p>Get your copy now for $45 delivered or Order it and pick it up at a Chamber Event for $35</p>
  <p>For Webinar information, become a member (currently free), subscribe to our newsletter (free) or check out our Community page.</p>
</div>

<!-- footer -->
<svg class="abs footer-band" viewBox="0 0 1200 431" width="1200" height="431" aria-hidden="true">
  <polygon points="0,95 1200,10 1200,431 0,431" fill="var(--navy)"/>
  <polygon points="0,100 1200,14 1200,19 0,105" fill="var(--gold)"/>
  <polygon points="0,112 1200,28 1200,31 0,115" fill="var(--white)"/>
</svg>

<div class="abs foot-col" style="left:107px;top:2437px">
  <h4 style="margin-bottom:16px">Contact Us</h4>
  <div class="contact-row"><svg width="14" height="16" viewBox="0 0 14 16" fill="none" stroke="#b9c3d3" stroke-width="1.4"><path d="M7 15s5-5 5-9A5 5 0 0 0 2 6c0 4 5 9 5 9z"/><circle cx="7" cy="6" r="1.8"/></svg><span>27 Harbour Lane<br>Varden QLD, 4207</span></div>
  <div class="contact-row"><svg width="16" height="16" viewBox="0 0 24 24" fill="none" stroke="#b9c3d3" stroke-width="2"><path d="M5 3h4l2 5-2.5 1.5a11 11 0 0 0 6 6L16 13l5 2v4a2 2 0 0 1-2 2A16 16 0 0 1 3 5a2 2 0 0 1 2-2z"/></svg><span>0412555019</span></div>
  <div class="contact-row"><svg width="16" height="12" viewBox="0 0 16 12" fill="none" stroke="#b9c3d3" stroke-width="1.4"><rect x="1" y="1" width="14" height="10"/><path d="M1 1l7 6 7-6"/></svg><span>hello@vardenchamber.com.au</span></div>
</div>
<div class="abs foot-col" style="left:382px;top:2440px">
  <h4>MEMBERSHIP</h4>
  <ul><li>Benefits</li><li>Community</li><li>Membership Directory</li></ul>
</div>
<div class="abs foot-col" style="left:615px;top:2440px">
  <h4>EVENTS</h4>
  <ul><li>Business Distinction Awards</li><li>Varden Business Expo</li><li>Events Schedule</li><li>Recordings</li><li>Business Distinction Awards</li><li>Varden Business Expo</li></ul>
</div>
<div class="abs foot-col" style="left:896px;top:2440px">
  <h4>ABOUT</h4>
  <ul><li>Contact</li><li>Committee</li><li>Past Committee Members</li><li>Terms</li><li>Privacy</li></ul>
</div>

<div class="abs foot-rule"></div>
<div class="abs copyright">Copyright 2020&nbsp; vardenchamber</div>
<div class="abs foot-social"><span></span><span></span><span></span></div>

</body>
</html>
```